Homepage sliders

We are a medical software company in the process of building our new site: http://www.staging.qvrdn.example/newsite/index.php
We would like three images for our homepage slider section. They would have to fit aesthetically into this section. The three sliders we had in mind:
-One slider showing multiple devices – a non-Brindle monitor, zTalker, Morvessa and eSlate
-One slider showing security (HIPAA compliancy)
-One slider showing multiple access points – at the hospital, at your practice, on the go
We do not want pictures of people. As inspiration, please use the current placeholder images on our homepage: http://www.staging.qvrdn.example/newsite/index.php
NOTE:
We are not looking for new slider designs. We only want images that would go into the current slider. Thank you!

```html
<!DOCTYPE html>
<html lang="en">
<head>
<meta charset="utf-8">
<title>Qoravan Medical — Homepage Slider</title>
<link href="https://fonts.googleapis.com/css2?family=Open+Sans:wght@400;600;700&family=Source+Sans+3:wght@400;600&display=swap" rel="stylesheet">
<style>
  :root {
    --nav-bg: #262c36;
    --nav-bg-edge: #1c2129;
    --nav-text: #ffffff;
    --brand-blue: #2f8fd8;
    --brand-blue-dark: #1f6fb4;
    --hero-bg-top: #ffffff;
    --hero-bg-bottom: #f3f3f3;
    --heading: #333333;
    --body-text: #3a3a3a;
    --cta-green: #6aa843;
    --cta-green-dark: #4e8a2c;
    --arrow-bg: #1e1e1e;
    --rule: #dcdcdc;
    --media-light: #e9ecef;
    --media-mid: #b9bfc6;
    --media-dark: #2a2d31;
  }
  * { box-sizing: border-box; margin: 0; padding: 0; }
  html, body { width: 1200px; height: 491px; overflow: hidden; background: var(--hero-bg-bottom); }
  body { position: relative; font-family: "Source Sans 3", "Helvetica Neue", Arial, sans-serif; }

  .site-header {
    position: absolute; left: 0; top: 0; width: 1200px; height: 59px;
    background: linear-gradient(180deg, var(--nav-bg), var(--nav-bg-edge));
    display: flex; align-items: center;
  }
  .brand {
    position: absolute; left: 80px; top: 13px;
    display: flex; align-items: center; gap: 9px;
    color: var(--nav-text); font-family: "Source Sans 3", sans-serif;
    font-weight: 600; font-size: 28px; line-height: 32px; text-decoration: none;
  }
  .brand-mark { width: 22px; height: 22px; background: var(--brand-blue); border-radius: 3px; }

  .main-nav { position: absolute; top: 0; left: 0; height: 59px; }
  .main-nav a {
    position: absolute; top: 22px; color: var(--nav-text); text-decoration: none;
    font-family: "Open Sans", sans-serif; font-weight: 600; font-size: 13.5px; line-height: 16px; white-space: nowrap;
  }
  .nav-products { left: 755px; }
  .nav-products .caret { display: inline-block; margin-left: 4px; vertical-align: 3px;
    border-left: 3.5px solid transparent; border-right: 3.5px solid transparent; border-top: 4px solid var(--nav-text); }
  .nav-faq { left: 847px; }
  .nav-security { left: 900px; }
  .nav-blog { left: 976px; }
  .main-nav .nav-cta {
    left: 1024px; top: 17px; width: 96px; height: 27px; line-height: 25px; text-align: center;
    background: linear-gradient(180deg, #3a9fe6, var(--brand-blue-dark));
    border: 1px solid #1a5f9c; border-radius: 4px; font-size: 13.5px;
  }

  .hero-slider {
    position: absolute; left: 0; top: 59px; width: 1200px; height: 419px;
    background: linear-gradient(180deg, var(--hero-bg-top), var(--hero-bg-bottom));
    border-bottom: 1px solid var(--rule);
  }
  .slide-media {
    position: absolute; left: 173px; top: 41px; width: 467px; height: 318px;
    border-radius: 8px;
    background: radial-gradient(ellipse at 50% 40%, var(--media-light) 0%, var(--media-mid) 65%, var(--media-dark) 100%);
  }
  .slide-copy { position: absolute; left: 680px; top: 84px; width: 340px; }
  .slide-title { font-weight: 600; font-size: 27px; line-height: 32px; color: var(--heading); }
  .slide-text { margin-top: 13px; font-size: 14.5px; line-height: 19.5px; color: var(--body-text); text-align: justify; }
  .slide-cta {
    display: inline-block; margin-top: 21px; width: 162px; height: 35px; line-height: 33px; text-align: center;
    background: linear-gradient(180deg, #7dbb55, var(--cta-green-dark));
    border: 1px solid #45782a; border-radius: 2px;
    color: #ffffff; font-size: 15px; font-weight: 400; text-transform: uppercase; text-decoration: none;
  }
  .slider-arrow { position: absolute; top: 188px; width: 27px; height: 27px; }
  .slider-arrow.prev { left: 84px; }
  .slider-arrow.next { left: 1091px; }
</style>
</head>
<body>
  <header class="site-header">
    <a class="brand" href="#"><span class="brand-mark"></span>Qoravan Medical</a>
    <nav class="main-nav">
      <a class="nav-products" href="#">Products<span class="caret"></span></a>
      <a class="nav-faq" href="#">FAQ</a>
      <a class="nav-security" href="#">Security</a>
      <a class="nav-blog" href="#">Blog</a>
      <a class="nav-cta" href="#">Get Started</a>
    </nav>
  </header>

  <section class="hero-slider">
    <div class="slide-media" role="img" aria-label="Desktop monitor, two phones and a tablet each showing the website on screen"></div>

    <div class="slide-copy">
      <h1 class="slide-title">Say Goodbye to Lost Charges!</h1>
      <p class="slide-text">There are many variations of passages of Lorem Ipsum available, but the majority have suffered alteration in some form, by injected humour, or randomised words which don't look.</p>
      <a class="slide-cta" href="#">Get Started Now!</a>
    </div>

    <svg class="slider-arrow prev" viewBox="0 0 27 27" aria-label="Previous slide">
      <circle cx="13.5" cy="13.5" r="13.5" fill="var(--arrow-bg)"/>
      <path d="M15.5 8.5 L10.5 13.5 L15.5 18.5" fill="none" stroke="#fff" stroke-width="2.6" stroke-linecap="round" stroke-linejoin="round"/>
    </svg>
    <svg class="slider-arrow next" viewBox="0 0 27 27" aria-label="Next slide">
      <circle cx="13.5" cy="13.5" r="13.5" fill="var(--arrow-bg)"/>
      <path d="M11.5 8.5 L16.5 13.5 L11.5 18.5" fill="none" stroke="#fff" stroke-width="2.6" stroke-linecap="round" stroke-linejoin="round"/>
    </svg>
  </section>
</body>
</html>
```